Presentation Folder, Business Card, Letterhead and Envelope design

We are a dental clinic that will open in August and we are looking for a professional graphic designer to create our Business Card, Presentation Folder, Letterhead, Notepad and envelopes.

The brand NovaGrin must reflect a sense of quality and sophistication, marketed for middle-class consumers.
Our preference is for quality and refined materials, where less is more.
Attached the logo

```html
<!DOCTYPE html>
<html lang="en">
<head>
<meta charset="utf-8">
<title>NovaGrin Presentation Folder</title>
<link rel="stylesheet" href="https://fonts.googleapis.com/css2?family=Raleway:wght@300;400&family=Roboto:wght@400&display=swap">
<style>
  :root {
    --backdrop: #d6d6d6;
    --paper: #ffffff;
    --paper-shade: #ececec;
    --brand-grey: #595959;
    --brand-red: #6b1012;
    --brand-red-deep: #4c0a0d;
    --text-grey: #4a4a4a;
  }
  * { margin: 0; padding: 0; box-sizing: border-box; }
  html, body {
    width: 1200px; height: 847px; overflow: hidden;
    background: var(--backdrop);
  }
  .folder-spread {
    position: absolute; left: 60px; top: 63px;
    width: 1080px; height: 720px;
    display: flex;
    box-shadow: 0 10px 30px rgba(0,0,0,0.25);
  }
  .panel { position: relative; width: 540px; height: 720px; overflow: hidden; }
  .back-cover {
    background: linear-gradient(120deg, var(--paper-shade) 0%, var(--paper) 40%, var(--paper-shade) 100%);
  }
  .front-cover { background: var(--paper); }
  .front-art { position: absolute; inset: 0; width: 540px; height: 720px; }
  .brand-name {
    position: absolute; top: 110px; left: 0; width: 540px;
    display: flex; align-items: center; justify-content: center; gap: 14px;
    font-family: "Raleway", sans-serif; font-weight: 300;
    font-size: 34px; letter-spacing: 8px; text-transform: uppercase;
    color: var(--paper);
  }
  .brand-square { width: 30px; height: 30px; background: var(--paper); }
  .front-url {
    position: absolute; top: 590px; left: 250px; width: 260px; text-align: center;
    font-family: "Raleway", sans-serif; font-weight: 400; font-size: 19px;
    color: var(--paper); letter-spacing: 0.5px;
  }
  .contact-block {
    position: absolute; left: 0; top: 560px; width: 540px;
    text-align: center;
    font-family: "Roboto", sans-serif; font-size: 14px; line-height: 1.6;
    color: var(--text-grey);
  }
  .contact-brand {
    display: inline-flex; align-items: center; gap: 8px; margin-bottom: 10px;
    font-family: "Raleway", sans-serif; font-weight: 300; font-size: 20px;
    letter-spacing: 4px; text-transform: uppercase; color: var(--brand-grey);
  }
  .contact-brand .mark { width: 18px; height: 18px; background: var(--brand-red); }
  .contact-line { display: flex; justify-content: center; align-items: center; gap: 14px; }
  .contact-item { display: inline-flex; align-items: center; gap: 5px; }
  .contact-item svg { width: 12px; height: 12px; fill: var(--brand-red); }
  .web-accent { color: var(--brand-red); }
</style>
</head>
<body>
  <main class="folder-spread">
    <section class="panel back-cover">
      <div class="contact-block">
        <div class="contact-brand"><span class="mark"></span>NovaGrin</div>
        <p>48 Maple Crest Road, Alderbrook Vale, WM 4K7</p>
        <p class="contact-line">
          <span class="contact-item">
            <svg viewBox="0 0 24 24"><path d="M6.6 10.8a15 15 0 0 0 6.6 6.6l2.2-2.2a1 1 0 0 1 1-.25 11.4 11.4 0 0 0 3.6.57 1 1 0 0 1 1 1V20a1 1 0 0 1-1 1A17 17 0 0 1 3 4a1 1 0 0 1 1-1h3.5a1 1 0 0 1 1 1c0 1.25.2 2.45.57 3.57a1 1 0 0 1-.25 1z"/></svg>
            555.204.1180
          </span>
          <span class="contact-item">
            <svg viewBox="0 0 24 24"><path d="M2 5h20v14H2z M2 5l10 8 10-8" stroke="#fff" stroke-width="1.5"/></svg>
            info@novagrin.com
          </span>
        </p>
        <p>www.<span class="web-accent">novagrin</span>.com</p>
      </div>
    </section>

    <section class="panel front-cover">
      <svg class="front-art" viewBox="0 0 540 720" aria-hidden="true">
        <defs>
          <linearGradient id="redField" x1="0" y1="0" x2="1" y2="0">
            <stop offset="0" stop-color="#6b1012"/>
            <stop offset="1" stop-color="#4c0a0d"/>
          </linearGradient>
          <linearGradient id="greyField" x1="0" y1="0" x2="1" y2="0">
            <stop offset="0.4" stop-color="#575757"/>
            <stop offset="1" stop-color="#6a6a6a"/>
          </linearGradient>
        </defs>
        <path d="M0 0 H540 V150 C 520 300, 320 400, 0 402 Z" fill="url(#greyField)"/>
        <path d="M0 545 C 260 520, 470 340, 540 135 V720 H0 Z" fill="url(#redField)"/>
      </svg>
      <div class="brand-name"><span class="brand-square"></span>NovaGrin</div>
      <p class="front-url">www.novagrin.com</p>
    </section>
  </main>
</body>
</html>
```